Web design for Money Service Business (uncoded)

We need a very basic website with 5-6 pages. Home page, Services, Transfer(How to use our service), About us, Contact us, FAQ
Our company name is Meridale Exchange. We are a company that deals with currency exchange and international money transfer. We do cash exchange and international money transfers to bank accounts all over the world. We offer highly competitive exchange rates so usually attract customers who transfer money over $10,000. Our niche is with larger sums of money, the design needs to be professional and communicate trust, security and stability.

```html
<!DOCTYPE html>
<html lang="en">
<head>
<meta charset="utf-8">
<title>Meridale Exchange — International Money Transfer</title>
<link href="https://fonts.googleapis.com/css2?family=Roboto:wght@300;400;500&display=swap" rel="stylesheet">
<style>
:root{
  --blue:#1c5a93;
  --navy:#143f6d;
  --orange:#f39a2e;
  --orange-deep:#ec8a1c;
  --ink:#222;
  --muted:#666;
  --panel:#f1f1f1;
  --line:#c9c9c9;
}
*{margin:0;padding:0;box-sizing:border-box}
html,body{width:1200px;height:893px;overflow:hidden}
body{position:relative;background:#fff;font-family:"Roboto",Arial,sans-serif;font-weight:300;color:var(--ink)}
.abs{position:absolute}

.brand{left:202px;top:20px}
.brand-name{font-size:38px;font-weight:400;color:var(--blue);letter-spacing:-0.5px;line-height:1}
.brand-tag{font-size:14px;font-weight:300;color:var(--blue);letter-spacing:3.6px;margin-top:6px}

.social{right:204px;top:31px;display:flex;gap:4px}
.social span{width:30px;height:30px;border-radius:50%;display:block}
.social .s1{background:#2ea3dc}.social .s2{background:var(--navy)}
.social .s3{background:#e1462f}.social .s4{background:var(--orange)}

.nav{left:202px;top:86px;width:795px;height:25px;background:var(--blue);display:flex}
.nav a{color:#fff;text-decoration:none;font-size:12px;font-weight:400;line-height:25px;display:block}
.nav .home{background:var(--orange);width:91px;text-align:center}
.nav .i2{margin-left:27px}.nav .i3{margin-left:55px}.nav .i4{margin-left:55px}.nav .i5{margin-left:55px}

.band{left:0;top:111px;width:1200px;height:327px;background:radial-gradient(ellipse at 20% 40%,#f7a945 0%,var(--orange) 45%,var(--orange-deep) 100%)}
.slide{left:203px;top:121px;width:795px;height:307px;border-radius:4px;background:linear-gradient(180deg,#ffffff 0%,#ececec 100%);box-shadow:0 1px 4px rgba(0,0,0,.25);overflow:hidden}
.slide-art{left:52px;top:10px;width:300px;height:288px;border-radius:6px;background:radial-gradient(circle at 50% 50%,#fbe3c2 0%,#e9eef7 45%,#d6e0f0 100%)}
.slide-title{left:445px;top:56px;font-size:25px;font-weight:300;color:var(--blue);line-height:26px;width:330px}
.slide-text{left:447px;top:124px;font-size:14.3px;line-height:18.3px;width:268px;color:#222}
.btn{left:447px;top:211px;width:173px;height:46px;background:linear-gradient(#1d5f9c,var(--navy));border-radius:3px;color:#fff;font-size:20px;font-weight:400;text-align:center;line-height:46px}
.arrow-btn{width:32px;height:32px;border-radius:50%;background:#2a2a2a;border:2px solid #555;top:258px}
.arrow-btn svg{display:block}
.prev{left:191px}.next{left:975px}

.rates{left:202px;top:453px;width:795px;height:22px;border:1px solid var(--line);background:#f6f6f6;font-size:10.5px;font-weight:400;color:var(--navy);line-height:20px;white-space:nowrap}
.rates span{position:absolute}
.rates b{font-weight:400;color:var(--orange)}

.welcome{left:203px;top:500px;width:470px}
.welcome h1{font-size:18.5px;font-weight:400;color:#222;margin-bottom:7px}
.welcome p{font-size:12.7px;line-height:16.9px;margin-bottom:5px}
.divider{left:688px;top:497px;height:170px;border-left:1px dotted #bbb}

.news{left:719px;top:500px;width:280px}
.news h2{font-size:15.5px;font-weight:400;margin-bottom:7px}
.news .date{font-size:13.5px;color:var(--blue);font-weight:300;margin-bottom:4px}
.news .head{font-size:11px;font-weight:400;margin-bottom:2px}
.news .sum{font-size:10.5px;color:var(--muted);margin-bottom:1px}
.news .more{font-size:11px;color:var(--blue);font-weight:400;margin-bottom:14px}

.offers{left:202px;top:706px;width:795px;height:104px;background:var(--panel);border:1px solid #d8d8d8}
.offers h3{position:absolute;left:8px;top:10px;font-size:17px;font-weight:300;color:var(--blue)}
.offers p{position:absolute;left:8px;top:36px;width:470px;font-size:11px;line-height:16.9px}
.offers .link{position:absolute;left:8px;top:84px;font-size:11.5px;font-weight:400}
.offers .photo{position:absolute;left:514px;top:6px;width:262px;height:92px;background:linear-gradient(160deg,#efe4dc,#d8a58f 45%,#6c7fae 80%,#ececec);border-radius:3px}

.foot{left:208px;top:836px}
.foot .copy{font-size:11.5px;font-weight:400}
.foot .copy .b{color:var(--blue)}
.foot small{display:block;font-size:8.5px;color:var(--muted);line-height:11px}
.badges{left:580px;top:850px;display:flex;gap:8px;align-items:center}
.badges span{display:block;height:18px;background:#d9dde4;border-radius:2px}
</style>
</head>
<body>

<div class="abs brand">
  <div class="brand-name">Meridale Exchange</div>
  <div class="brand-tag">INTERNATIONAL MONEY TRANSFER</div>
</div>

<div class="abs social" aria-label="Social links">
  <span class="s1"></span><span class="s2"></span><span class="s3"></span><span class="s4"></span>
</div>

<nav class="abs nav">
  <a class="home" href="#">Home</a>
  <a class="i2" href="#">Services</a>
  <a class="i3" href="#">Transfer</a>
  <a class="i4" href="#">About Us</a>
  <a class="i5" href="#">Contact Us</a>
</nav>

<div class="abs band"></div>

<div class="abs slide">
  <div class="abs slide-art" role="img" aria-label="Illustration of world currencies flowing into the exchange"></div>
  <div class="abs slide-title">We offer highly competitive exchange rates</div>
  <div class="abs slide-text">Lorem Ipsum is simply dummy text of the printing and typesetting industry. Lorem Ipsum has been the industry’s standard dummy text ever since the 1500s.</div>
  <div class="abs btn">LEARN MORE</div>
</div>

<div class="abs arrow-btn prev"><svg width="28" height="28" viewBox="0 0 28 28"><path d="M16 9 L11 14 L16 19" fill="none" stroke="#fff" stroke-width="2.4"/></svg></div>
<div class="abs arrow-btn next"><svg width="28" height="28" viewBox="0 0 28 28"><path d="M12 9 L17 14 L12 19" fill="none" stroke="#fff" stroke-width="2.4"/></svg></div>

<div class="abs rates">
  <span style="left:9px">GBP/CAD = <b>1.7128</b></span>
  <span style="left:116px">GBP/CZK = <b>32.6650</b></span>
  <span style="left:227px">GBP/DKK = <b>8.9320</b></span>
  <span style="left:341px">GBP/HKD = <b>12.5660</b></span>
  <span style="left:461px">GBP/CZK = <b>32.6650</b></span>
  <span style="left:580px">GBP/DKK = <b>8.9320</b></span>
  <span style="left:686px">GBP/HKD = <b>12.5660</b></span>
</div>

<section class="abs welcome">
  <h1>Welcome to Our Website</h1>
  <p>Lorem Ipsum is simply dummy text of the printing and typesetting industry. Lorem Ipsum has been the industry’s standard dummy text ever since the 1500s, when an unknown printer took a galley of type and scrambled it to make a type specimen book. It has survived not only five centuries, but also the leap into electronic typesetting, remaining essentially unchanged.</p>
  <p>It was popularised in the 1960s with the release of Lettrafix sheets containing Lorem Ipsum passages, and more recently with desktop publishing software like Pressline Composer including versions of Lorem Ipsum.</p>
</section>

<div class="abs divider"></div>

<aside class="abs news">
  <h2>Latest News</h2>
  <div class="date">November 25, 2013</div>
  <div class="head">Lorem Ipsum is simply dimmy text.</div>
  <div class="sum">Lorem Ipsum is simply dummy text of the printing press.</div>
  <div class="more">+ Read More</div>
  <div class="date">November 24, 2013</div>
  <div class="head">Lorem Ipsum is simply dimmy text.</div>
  <div class="sum">Lorem Ipsum is simply dummy text.</div>
  <div class="more">+ Read More</div>
</aside>

<section class="abs offers">
  <h3>Our Discounts Offers</h3>
  <p>Lorem Ipsum is simply dummy text of the printing and typesetting industry. Lorem Ipsum has been the industry’s standard dummy text ever since the 1500s, when an unknown printer took a galley of type and scrambled it to make a type specimen book.</p>
  <div class="link">Learn More</div>
  <div class="photo" role="img" aria-label="Photo of banknotes and bank cards"></div>
</section>

<footer class="abs foot">
  <div class="copy">© 2013 <span class="b">Meridale Exchange</span> | All Rights Reserved.</div>
  <small>Lorem Ipsum is simply dummy text of the printing and typesetting industry.</small>
  <small>Lorem Ipsum has been the industry’s standard dummy text ever since the 1500s</small>
</footer>

<div class="abs badges" aria-label="Accepted payment methods">
  <span style="width:30px"></span><span style="width:26px"></span><span style="width:28px"></span>
  <span style="width:26px"></span><span style="width:14px"></span><span style="width:26px"></span>
  <span style="width:34px"></span><span style="width:40px"></span><span style="width:50px"></span>
  <span style="width:58px"></span>
</div>

</body>
</html>
```